CORVID PRESS - Trade Show Flyer

Tri-fold brochure for trade show and follow-up mailings. Need design to mirror web-site look and feel. Use same color scheme of the blue and green. Please use a consistent font throughout. I like blocks of color or using the green/blue as border or trim.See the attachment for additional details, including specifications and content required.
Updates

Project Deadline Extended
Reason: Extended due to travel - company meetings

Target Market(s)

Business Professionals

Industry/Entity Type

Trade

Font styles to use
Serif
Sans Serif

Colors

Designer to choose colors to be used in the design.

Requirements
Must have
• A clean look and feel that matches our web-site
• Not too busy, white space is a plus
• Good use of color - blue and green (please match to web-site and attached logo colors)
Nice to have
• Icons or photos to break up the text
Should not have
• Should not be too busy or crowded. In the attached brief sheet, I included a section that can be removed if there is too much content.

```html
<!DOCTYPE html>
<html lang="en">
<head>
<meta charset="utf-8">
<title>Corvid Press – Trade Show Brochure</title>
<link rel="stylesheet" href="https://fonts.googleapis.com/css2?family=Open+Sans:wght@400;600;700&display=swap">
<style>
  :root{
    --canvas:#ececec;
    --paper:#ffffff;
    --blue:#1f5c99;
    --blue-deep:#163f6e;
    --teal:#2f9e9a;
    --green:#48b58a;
    --ink:#3a4a5a;
    --muted:#7d8a96;
    --photo-cool:#8fa3b8;
    --photo-warm:#c9b8aa;
  }
  *{box-sizing:border-box;margin:0;padding:0}
  html,body{width:1200px;height:2400px;overflow:hidden;background:var(--canvas);font-family:"Open Sans",Arial,sans-serif}
  .spread{position:absolute;left:40px;width:1120px;height:866px;display:flex;box-shadow:0 6px 24px rgba(0,0,0,.12);background:var(--paper)}
  .spread--outside{top:200px}
  .spread--inside{top:1300px}
  .panel{position:relative;width:373.33px;height:100%;overflow:hidden}
  .photo{position:absolute;left:0;width:100%}
  .panel--back{background:var(--blue);color:#fff}
  .panel--back .photo{top:0;height:250px;background:linear-gradient(160deg,#d8e2ea,#9fb2c4 60%,#6f8aa5)}
  .badge-circle{position:absolute;left:50%;top:210px;width:86px;height:86px;margin-left:-43px;border-radius:50%;background:#fff;border:5px solid var(--green)}
  .back-copy{position:absolute;top:330px;left:40px;right:40px}
  .heading-light{font-size:22px;font-weight:700;margin-bottom:16px}
  .body-light{font-size:14px;line-height:1.65;margin-bottom:14px;color:#e3ecf5}
  .panel--flap{background:linear-gradient(180deg,var(--teal),var(--green));color:#fff;padding:90px 42px 0}
  .flap-title{font-size:26px;font-weight:700;line-height:1.25;margin-bottom:22px}
  .rule{width:60px;height:3px;background:#fff;margin-bottom:22px}
  .cta{display:block;border:2px solid #fff;border-radius:4px;padding:12px 16px;font-size:15px;font-weight:600;margin-bottom:16px;text-align:center}
  .flap-note{margin-top:30px;font-size:13px;color:#e8f6f0;text-align:center}
  .panel--cover{background:var(--paper)}
  .brand{position:absolute;top:60px;right:40px;display:flex;align-items:center;gap:12px}
  .brand-mark{width:22px;height:22px;background:var(--green)}
  .brand-name{font-size:28px;font-weight:700;color:var(--blue);letter-spacing:1px}
  .panel--cover .photo{top:150px;height:470px;background:linear-gradient(180deg,#f2eee9,var(--photo-warm) 55%,#8fa6bd)}
  .cover-caption{position:absolute;top:650px;left:0;right:0;text-align:center;font-size:16px;color:var(--ink);font-weight:600}
  .cover-band{position:absolute;bottom:60px;left:30px;right:30px;background:var(--blue);color:#fff;text-align:center;padding:16px;font-size:16px;font-weight:600;border-left:8px solid var(--green)}
  .panel--advantage{background:var(--blue-deep);color:#fff;padding:60px 40px 0}
  .subheading-light{font-size:16px;font-weight:700;color:var(--green);margin:22px 0 12px}
  .tick-list{list-style:none}
  .tick-list li{display:flex;align-items:center;gap:10px;font-size:14px;margin-bottom:10px;color:#e3ecf5}
  .panel--advantage .photo{bottom:0;height:300px;background:linear-gradient(180deg,#b9c7d4,var(--photo-warm) 60%,#59708a)}
  .panel--approach{background:var(--paper)}
  .panel--approach .photo{top:0;height:280px;background:linear-gradient(160deg,#e7ecf1,#a9bccd 60%,#7f98b0)}
  .icon-disc{position:absolute;left:50%;top:236px;width:90px;height:90px;margin-left:-45px;border-radius:50%;background:#fff;border:5px solid var(--blue);display:flex;align-items:center;justify-content:center}
  .approach-copy{position:absolute;top:360px;left:40px;right:40px;text-align:center}
  .heading-dark{font-size:22px;font-weight:700;color:var(--blue);margin-bottom:16px}
  .body-dark{font-size:14px;line-height:1.7;color:var(--ink);margin-bottom:14px}
  .panel--services{background:var(--paper);border-left:1px solid #e3e7eb}
  .panel--services .photo{top:0;height:220px;background:linear-gradient(160deg,#f0f0ee,#c7cfd6 55%,#95a8ba)}
  .service-list{position:absolute;top:260px;left:36px;right:36px;list-style:none}
  .service{display:flex;gap:14px;margin-bottom:30px}
  .service-icon{flex:none;width:44px;height:44px;border-radius:50%;background:var(--green);display:flex;align-items:center;justify-content:center}
  .service-title{font-size:16px;font-weight:700;color:var(--blue);margin-bottom:4px}
  .service-text{font-size:13px;line-height:1.55;color:var(--muted)}
  .services-band{position:absolute;bottom:0;left:0;right:0;height:120px;background:linear-gradient(90deg,var(--blue),var(--teal));color:#fff;display:flex;align-items:center;justify-content:center;font-size:20px;font-weight:700}
</style>
</head>
<body>

<section class="spread spread--outside">
  <div class="panel panel--back">
    <div class="photo" role="img" aria-label="Photo of a bright modern office interior"></div>
    <div class="badge-circle"></div>
    <div class="back-copy">
      <h2 class="heading-light">Who we are</h2>
      <p class="body-light">We help brands tell clear stories in print and online, from first idea to final delivery.</p>
      <p class="body-light">Our team blends strategy, design and production under one roof.</p>
    </div>
  </div>

  <div class="panel panel--flap">
    <h2 class="flap-title">We're built for busy teams</h2>
    <div class="rule"></div>
    <p class="body-light">Planning a show or a launch? We keep every piece on brand and on time.</p>
    <span class="cta">Request a quote</span>
    <span class="cta">Book a meeting</span>
    <p class="flap-note">Contact us today</p>
  </div>

  <div class="panel panel--cover">
    <div class="brand"><span class="brand-mark"></span><span class="brand-name">CORVID PRESS</span></div>
    <div class="photo" role="img" aria-label="Photo of business people walking through a sunlit hall"></div>
    <p class="cover-caption">Print, Design &amp; Media Services</p>
    <div class="cover-band">Your partner at every stage</div>
  </div>
</section>

<section class="spread spread--inside">
  <div class="panel panel--advantage">
    <h2 class="heading-light">See the competitive advantage</h2>
    <p class="body-light">Clients choose us for speed, care and results they can measure.</p>
    <h3 class="subheading-light">What sets us apart</h3>
    <ul class="tick-list">
      <li><svg width="16" height="16" viewBox="0 0 16 16"><path d="M2 8l4 4 8-8" fill="none" stroke="#48b58a" stroke-width="2.5"/></svg>Fast turnaround</li>
      <li><svg width="16" height="16" viewBox="0 0 16 16"><path d="M2 8l4 4 8-8" fill="none" stroke="#48b58a" stroke-width="2.5"/></svg>Dedicated account lead</li>
      <li><svg width="16" height="16" viewBox="0 0 16 16"><path d="M2 8l4 4 8-8" fill="none" stroke="#48b58a" stroke-width="2.5"/></svg>Print and digital in one</li>
    </ul>
    <div class="photo" role="img" aria-label="Photo of a smiling business team around a tablet"></div>
  </div>

  <div class="panel panel--approach">
    <div class="photo" role="img" aria-label="Photo of a glass office corridor"></div>
    <div class="icon-disc">
      <svg width="40" height="40" viewBox="0 0 40 40"><path d="M8 21l8 8 16-17" fill="none" stroke="#1f5c99" stroke-width="4" stroke-linecap="round" stroke-linejoin="round"/></svg>
    </div>
    <div class="approach-copy">
      <h2 class="heading-dark">Our approach</h2>
      <p class="body-dark">We listen first, then shape a plan that fits your goals and budget.</p>
      <p class="body-dark">Each project gets a clear timeline and regular updates.</p>
    </div>
  </div>

  <div class="panel panel--services">
    <div class="photo" role="img" aria-label="Photo of a meeting room with a laptop"></div>
    <ul class="service-list">
      <li class="service">
        <span class="service-icon"><svg width="20" height="20" viewBox="0 0 20 20"><path d="M4 10l4 4 8-8" fill="none" stroke="#fff" stroke-width="2.5"/></svg></span>
        <div><p class="service-title">Strategy</p><p class="service-text">Focused plans that drive growth.</p></div>
      </li>
      <li class="service">
        <span class="service-icon"><svg width="20" height="20" viewBox="0 0 20 20"><path d="M4 10h12M11 5l5 5-5 5" fill="none" stroke="#fff" stroke-width="2.5"/></svg></span>
        <div><p class="service-title">Design</p><p class="service-text">Clean layouts that stay on brand.</p></div>
      </li>
      <li class="service">
        <span class="service-icon"><svg width="20" height="20" viewBox="0 0 20 20"><path d="M4 10l4 4 8-8" fill="none" stroke="#fff" stroke-width="2.5"/></svg></span>
        <div><p class="service-title">Production</p><p class="service-text">Quality print delivered on schedule.</p></div>
      </li>
    </ul>
    <div class="services-band">Let's get started</div>
  </div>
</section>

</body>
</html>
```